Vantor Ridge military/warrior themed clothing company**

eCommerce clothing website

We do have a Shopify account that we would ups like this to be built on for it obvious reasons

We will be starting with the gym/casual wear “Vantor” it will be military style with a unique logo as well as military colours. We will sell this as an exclusive range limited edition to create a scarcity principle which hopefully has our customer desperate to get their gear. We will have it in the colours that Army, Navy and Airforce wear as their undershirts and PT shirts as this will create some great genuine military and KPWR Security origins. Exclusivity is the key.

Having a similar business model and advertising as PulseOtter who have done incredibly well in this area. Our story is better and we just study what sells and how they sell it. Focused on tops namely shirts and singlet and not 1000 choices keep it simple as simple is best and it sells.

Our story

• Veteran Security Company that requires our staff to keep in shape to provide the community with the best service
• No other brands or designers were up to the task of our military styled training, it all thinned, ripped, and looked terrible
• Decided if it’s broken, fix it and do it ourselves
• Trialed and tested every material and design on the market with extensive hours in the gym, outdoor PT, beach sessions, hill runs, boot camps, go till you puke and we did
• Found what worked and put it into action with a limited order just for our staff
• Some of the boys are still servicing and wore the gear to base PT and their fellow serving members wanted to get some of their own gear to which me made limited orders
• Created purpose PT gear with suitable colour scheme to conform with military regs so the boys no longer got in trouble, made limited orders
• Friends and family really liked the gear so after relentless persistence we gave in and made limited orders
• While performing volunteer advocacy work at the KDMs fellow veterans loved the designs and begged for their own gear which would give them confidence and motivation to get back in the gym to rehabilitate and get their health back, it was a no brainer we made limited order
• We began sponsoring local up and coming athletes, fighters and body builders so they could pursue their dream of becoming a professional in their craft again limited orders were made
• Though more relentless desire to obtain our brand and come onboard with our mission statement influencers and celebrities a like urged to endorse and become brand ambassadors so every Australian could feel what it was like to be apart of a genuine grass roots community that had a great story behind it
• And with that Vantor was born
• Stay tuned for the next exciting instalment of what’s to come as we don’t believe in reinventing the wheel but smashing it down completely

A comprehensive range that targets men and women of all ages, fitness levels, body shapes and their specific needs for all times with an exclusive veterans range to support the veteran community.

Top gym brands
Pulse otter
VORN
Tallow brook
Zuma
Omerel
Tavlin

Target Market(s)

men and women 30-45

Industry/Entity Type

Clothing

Number of Pages Required

5+ page

Font styles to use
Sans Serif

Requirements
Must have
• Home page
• white clean back ground
• menu in the top right corner
• search function
• Vantor lettering up the top nice and clean in black
• crisp Vantor shot of the first shoot in both the black and white gold
• headline "forge your legacy" comes across the bottom of the shot above
• men's lifestyle wear section - pre-order now - hyperlink to casual section
• men's active wear section - pre-order now - hyperlink to fitness section
• women's range - coming soon - hyperlink to women's section
• socials and contact (Facebook, Instagram)

Page 2
• our mission
• our story
• our values

Page 3
Change to lifestyle
Follow the format below for order
Functionality to allow pre-order sales for out of stock units

• men's casual wear
- casual singlets
- casual tees
- casual crews
- casual hoodies
- pre-order now

Page 4
Change to active wear

• men's fitness wear
- fitness tees
- fitness crews
- fitness hoodies
- pre-order now

Page 5
• women's section
- coming soon

Australian owed
Australian made
Australian benefit

Throw in an Australian flag

The whole idea was to be bringing in pre-order sales as we wait for the first order to come in from supplier and the next photo shoot we can simply update all the stock pics as needed. For now I have the tec-pac pics that can go in the product pages.

Mission

Building an unstoppable force of warriors that strive for perfection in every aspect of their lives to forge a legacy

Concept

Vantor is an unstoppable force that protect and inspire their own.

Vantor clothing is battle armour to wear as you take the hardest aspects of life to task.

From our struggle comes our resolve.

Tribute

Our fallen warriors and heroes that have come before us, making the ultimate sacrifice, that has allowed our lives to be free and liberated for an unencumbered pursuit of happiness

Story
• Australian family owned and operated
• Veteran led and staffed
• Created to protect those who protect us
• Tried and tested under military conditions
• Australian sourced and produced
• Ethical and environmentally friendly materials
• Restoration of Australian Pride

Values
• Culture
• Community
• Patriotism
• Honour
• Honesty
• Integrity
• Loyalty
• Courage
• Team work
• Success
Nice to have
• To look and feel like one of the big competitors with ease of navigation and ordering
Should not have
• clutter and loading issues

```html
<!DOCTYPE html>
<html lang="en">
<head>
<meta charset="utf-8">
<title>Vantor — Forge Your Legacy</title>
<link rel="stylesheet" href="https://fonts.googleapis.com/css2?family=Anton&family=Arimo:wght@400;700&display=swap">
<style>
:root{
  --ink:#0d0d0d;
  --slate:#414958;
  --slate-ghost:#4d5566;
  --slate-text:#4a5366;
  --muted:#9aa1ad;
  --rule:#d7dadf;
  --hero-dark:#141414;
  --photo-light:#eef0f3;
  --bar:#2b2f36;
  --white:#ffffff;
}
*{box-sizing:border-box;margin:0;padding:0}
html,body{width:1200px;height:2997px;overflow:hidden;background:var(--white)}
body{position:relative;font-family:"Arimo",Arial,sans-serif;color:var(--ink)}
.abs{position:absolute}
.condensed{font-family:"Anton",Impact,sans-serif;letter-spacing:3px}

/* header */
.brand{left:60px;top:34px;font-size:58px;letter-spacing:6px;color:var(--ink);line-height:1}
.search{left:601px;top:58px;width:314px;height:32px;border-bottom:2px solid var(--rule);font-size:16px;color:#666}
.search svg{position:absolute;right:4px;top:0}
.account-block{left:961px;top:0;width:111px;height:149px;background:var(--slate)}
.cart-count{left:944px;top:29px;width:32px;height:32px;border:1.5px solid var(--ink);border-radius:50%;background:var(--white);font-size:15px;text-align:center;line-height:29px}
.menu{left:1116px;top:56px}

/* hero */
.hero{left:0;top:149px;width:1200px;height:602px;background:radial-gradient(ellipse at 50% 45%,#3a3a3a 0%,#1c1c1c 45%,var(--hero-dark) 100%)}
.hero-figure{left:410px;top:175px;width:330px;height:490px;border-radius:120px 120px 20px 20px;background:linear-gradient(#4a4541,#3b3b3b)}
.headline-card{left:124px;top:659px;width:951px;height:160px;background:var(--white);box-shadow:0 18px 22px -10px rgba(0,0,0,.28);text-align:center}
.headline-card h1{font-family:"Anton",Impact,sans-serif;font-weight:400;font-size:66px;letter-spacing:9px;line-height:160px;margin-top:-10px}
.intro{left:150px;top:860px;width:900px;text-align:center;font-size:15px;line-height:18px;letter-spacing:.5px;color:#333}

/* active wear */
.band{left:124px;top:983px;width:948px;height:102px;background:var(--slate)}
.ghost{color:var(--slate-ghost);font-size:70px;letter-spacing:26px}
.feature-photo{left:149px;top:975px;width:460px;height:473px;background:linear-gradient(135deg,#f4f5f8,var(--photo-light));box-shadow:0 22px 24px -14px rgba(0,0,0,.35)}
.feature-title{left:702px;top:1001px;font-size:60px;color:var(--white);letter-spacing:4px}
.feature-sub{left:702px;top:1095px;font-size:42px;letter-spacing:2px}
.feature-copy{left:704px;top:1158px;width:380px;font-size:13.5px;line-height:26.5px;letter-spacing:.4px;color:#333}
.btn{display:block;text-align:center;font-size:22px;letter-spacing:1.5px;border:1.5px solid var(--ink)}
.btn-feature{left:702px;top:1278px;width:257px;height:56px;line-height:53px}

/* collections */
.collection{top:1613px;width:455px;height:483px;background:var(--slate);color:var(--white)}
.collection .ghost{position:absolute;left:42px;top:30px;font-size:52px;letter-spacing:15px}
.collection h2{position:absolute;top:118px;font-family:"Anton",Impact,sans-serif;font-weight:400;font-size:62px;letter-spacing:5px}
.collection h3{position:absolute;top:210px;font-weight:400;font-size:40px;letter-spacing:1px}
.collection .btn{position:absolute;top:304px;width:257px;height:66px;line-height:63px;border-color:var(--white);color:var(--white)}

/* about strip */
.brand-foot{left:149px;top:2252px;font-size:58px;letter-spacing:6px;line-height:1}
.blurb{left:527px;top:2250px;width:540px;font-size:21px;line-height:29px;color:var(--slate-text)}
.rule{left:124px;top:2376px;width:951px;height:1px;background:var(--rule)}
.rule-accent{left:476px;top:2374px;width:83px;height:4px;background:var(--slate)}
.partner{top:2426px;font-size:21px;color:#b7bec8;font-weight:700;display:flex;align-items:center;gap:8px}
.partner i{display:inline-block;width:26px;height:26px;border-radius:50%;background:#c9ced6}

/* contact */
.contact-title{left:0;width:1180px;top:2575px;text-align:center;font-size:44px;color:var(--slate-text)}
.contact-sub{left:0;width:1180px;top:2656px;text-align:center;font-size:17px;color:#555}
.channel{top:2733px;width:160px;margin-left:-80px;text-align:center}
.channel .dot{width:72px;height:72px;border-radius:50%;background:var(--slate);margin:0 auto;display:flex;align-items:center;justify-content:center}
.channel .label{margin-top:14px;font-size:13px;color:#444}
.channel .value{margin-top:9px;font-size:11px;color:#a3a8b0}
.footer-links{left:137px;top:2895px;font-size:13.5px;color:#333;word-spacing:2px}
.footer-links span{margin:0 14px;color:#777}
.bottom-bar{left:0;top:2948px;width:1200px;height:49px;background:var(--bar);color:#b5b9c0;font-size:13px;text-align:center;line-height:49px}
</style>
</head>
<body>

<header>
  <div class="abs brand">VANTOR</div>
  <div class="abs search">Search our store
    <svg width="44" height="22" viewBox="0 0 44 22" fill="none" stroke="#555" stroke-width="3"><circle cx="11" cy="12" r="7"/><circle cx="33" cy="12" r="7"/><path d="M18 12h8"/></svg>
  </div>
  <div class="abs account-block">
    <svg class="abs" style="left:40px;top:24px" width="32" height="38" viewBox="0 0 32 38" fill="none" stroke="#fff" stroke-width="2"><rect x="2" y="11" width="28" height="25" rx="2"/><path d="M10 11V7a6 6 0 0 1 12 0v4"/></svg>
    <svg class="abs" style="left:41px;top:96px" width="30" height="32" viewBox="0 0 30 32" fill="none" stroke="#fff" stroke-width="2.5"><circle cx="15" cy="9" r="7"/><path d="M2 31c1-8 6-12 13-12s12 4 13 12"/></svg>
  </div>
  <div class="abs cart-count">3</div>
  <svg class="abs menu" width="42" height="34" viewBox="0 0 42 34" fill="var(--slate)"><rect width="42" height="7"/><rect y="13" width="42" height="7"/><rect y="27" width="42" height="7"/></svg>
</header>

<section>
  <div class="abs hero" role="img" aria-label="Campaign photo: athlete wearing a charcoal Vantor tee against a dark backdrop"></div>
  <div class="abs hero-figure" role="img" aria-label="Model in charcoal branded tee"></div>
  <div class="abs headline-card"><h1>FORGE YOUR LEGACY</h1></div>
  <p class="abs intro">A comprehensive range that targets men and women of all ages, fitness levels, body shapes and their specific needs for all times with an exclusive veterans range to support the veteran community.</p>
</section>

<section>
  <div class="abs band">
    <div class="abs condensed ghost" style="left:500px;top:8px;white-space:nowrap">THE WEAR</div>
  </div>
  <div class="abs feature-photo" role="img" aria-label="Model in black long-sleeve compression top, shorts and tights"></div>
  <div class="abs condensed feature-title">MEN</div>
  <svg class="abs" style="left:628px;top:1110px" width="16" height="16" viewBox="0 0 16 16" fill="none" stroke="#111" stroke-width="1.8"><path d="M14 8H2M7 3 2 8l5 5"/></svg>
  <div class="abs feature-sub">ACTIVE WEAR</div>
  <p class="abs feature-copy">Lorem ipsum dolor sit amet, consectetur adipiscing elit, sed do eiusmod tempor incididunt ut labore et dolore magna aliqua. Ut enim ad minim veniam,</p>
  <a class="abs btn btn-feature">PRE ORDER NOW</a>
</section>

<section>
  <div class="abs collection" style="left:124px">
    <div class="condensed ghost">COLLECTION</div>
    <h2 style="left:60px">WOMEN’S</h2>
    <h3 style="left:60px">RANGE</h3>
    <a class="btn" style="left:91px">COMING SOON</a>
  </div>
  <div class="abs collection" style="left:622px">
    <div class="condensed ghost">COLLECTION</div>
    <h2 style="left:37px">MEN</h2>
    <h3 style="left:37px">LIFE STYLE WEAR</h3>
    <a class="btn" style="left:93px">PRE ORDER NOW</a>
  </div>
</section>

<section>
  <div class="abs brand-foot">VANTOR</div>
  <p class="abs blurb">How many times have you been looking for a product, and seen a couple of options on a website, and thought, ‘what’s the difference?’. I’d guess many…</p>
  <div class="abs rule"></div>
  <div class="abs rule-accent"></div>
  <div class="abs partner" style="left:137px"><i></i>labore</div>
  <div class="abs partner" style="left:305px"><i></i>aliqua</div>
  <div class="abs partner" style="left:466px;color:var(--slate)"><i style="background:var(--slate)"></i>dynamic</div>
  <div class="abs partner" style="left:636px"><i></i>fugiat</div>
  <div class="abs partner" style="left:778px"><i></i>MAGNA</div>
  <div class="abs partner" style="left:963px">Frésh</div>
</section>

<section>
  <h2 class="abs contact-title" style="font-weight:400">Contact us</h2>
  <p class="abs contact-sub">We'd love to hear from you</p>

  <div class="abs channel" style="left:264px">
    <div class="dot"><svg width="18" height="14" viewBox="0 0 18 14" fill="#fff"><rect width="18" height="14" rx="2"/><path d="M1 2l8 6 8-6" stroke="#414958" stroke-width="1.6" fill="none"/></svg></div>
    <div class="label">Email</div><div class="value">hello@vantor.au</div>
  </div>
  <div class="abs channel" style="left:427px">
    <div class="dot"><svg width="16" height="16" viewBox="0 0 16 16" fill="#fff"><path d="M3 1l3 0 1.5 4-2 1.5a9 9 0 0 0 4 4L11 8.5l4 1.5v3c0 1-1 2-2 2C7 15 1 9 1 3c0-1 1-2 2-2z"/></svg></div>
    <div class="label">Phone</div><div class="value">555-010-0142</div>
  </div>
  <div class="abs channel" style="left:590px">
    <div class="dot"><svg width="14" height="18" viewBox="0 0 14 18" fill="#fff"><path d="M7 0a7 7 0 0 1 7 7c0 5-7 11-7 11S0 12 0 7a7 7 0 0 1 7-7z"/><circle cx="7" cy="7" r="2.5" fill="#414958"/></svg></div>
    <div class="label">Address</div><div class="value">18 Calder Lane, Sydney</div>
  </div>
  <div class="abs channel" style="left:752px">
    <div class="dot"></div>
    <div class="label">Insta</div><div class="value">@user_name</div>
  </div>
  <div class="abs channel" style="left:914px">
    <div class="dot"></div>
    <div class="label">Facebook</div><div class="value">@user_name</div>
  </div>
</section>

<footer>
  <nav class="abs footer-links">Home<span>|</span>Men’s Active Wear<span>|</span>Men’s Life Style Wear<span>|</span>Women’s Range<span>|</span>Terms &amp; Conditions<span>|</span>Returns &amp; Shipping.<span>|.</span>Privacy Policy</nav>
  <div class="abs bottom-bar">Copyright @ 2021, all rights reserved</div>
</footer>

</body>
</html>
```